Stunning website design for world's unique software

Design only (No coding required)
This website design is linked with a logo design and illustration design contests.

Industry/Entity Type

Software

```html
<!DOCTYPE html>
<html lang="en">
<head>
<meta charset="utf-8">
<title>vextra – Unique Experiences for Web &amp; Mobile</title>
<link href="https://fonts.googleapis.com/css2?family=Oswald:wght@300;400;500&family=Arimo:wght@400;700&display=swap" rel="stylesheet">
<style>
:root{
  --orange:#f7a600;
  --orange-deep:#f08a00;
  --ink:#333333;
  --text:#666666;
  --muted:#888888;
  --light:#f0f0f0;
  --header:#f4f4f4;
  --footer:#333333;
  --footer-line:#4a4a4a;
  --white:#ffffff;
}
*{box-sizing:border-box;margin:0;padding:0}
html,body{width:960px;height:1200px;overflow:hidden}
body{position:relative;background:var(--white);font-family:"Arimo",Arial,sans-serif;color:var(--text)}
.abs{position:absolute}
.display{font-family:"Oswald",Arial,sans-serif}

/* header */
.site-header{left:0;top:0;width:960px;height:78px;background:var(--header)}
.brand{left:93px;top:17px;display:flex;align-items:center;gap:8px}
.brand-dot{width:34px;height:34px;border-radius:50%;background:var(--orange)}
.brand-name{font-family:"Arimo",Arial,sans-serif;font-weight:700;font-size:30px;color:var(--ink);letter-spacing:0.5px}
.main-nav{left:409px;top:21px;display:flex}
.main-nav a{font-family:"Oswald",Arial,sans-serif;font-size:16px;color:#555;text-decoration:none;height:33px;line-height:33px;margin-right:47px}
.main-nav a.active{background:var(--orange);color:var(--white);width:75px;text-align:center;margin-right:30px}

/* hero */
.hero{left:0;top:78px;width:960px;height:250px;background:linear-gradient(100deg,#3a2c22 0%,#6a4a34 45%,#4b3628 70%,#8a5a36 100%)}
.hero-title{left:93px;top:148px;font-family:"Oswald",Arial,sans-serif;font-weight:300;font-size:32px;line-height:42px;color:var(--white);text-transform:uppercase;letter-spacing:-0.5px}
.hero-devices{left:428px;top:98px;width:436px;height:222px;border-radius:8px;background:linear-gradient(180deg,#d8d8d8,#9a9a9a)}

/* features */
.feature{width:400px}
.feature-icon{width:58px;height:58px;border-radius:50%;background:var(--orange);display:flex;align-items:center;justify-content:center}
.feature-title{font-family:"Oswald",Arial,sans-serif;font-size:20px;color:var(--ink);line-height:26px}
.feature-text{font-size:11.5px;line-height:18.3px;letter-spacing:0.6px;color:var(--text);width:325px;margin-top:4px}

/* options */
.options{left:0;top:575px;width:960px;height:250px;background:var(--light)}
.options-shot{left:67px;top:583px;width:362px;height:235px;background:linear-gradient(180deg,#e6e6e6,#d2d2d2)}
.circle-icon{width:42px;height:42px;border-radius:50%;background:var(--orange);display:flex;align-items:center;justify-content:center}
.section-title{font-family:"Oswald",Arial,sans-serif;font-size:20px;color:var(--ink);line-height:24px}
.section-title .hl{color:var(--orange);font-weight:300}
.options-text{font-size:10.8px;line-height:18.3px;color:var(--text);width:395px}
.check-list{list-style:none;font-size:10.8px;color:var(--text)}
.check-list li{display:flex;align-items:center;gap:6px;height:20.6px}
.learn-more{font-family:"Oswald",Arial,sans-serif;font-size:15px;color:var(--orange-deep);text-decoration:underline}

/* testimonials */
.testimonial-photo{width:68px;height:66px;background:linear-gradient(180deg,#e9e4df,#cfc6bc)}
.quote-text{font-size:10.8px;line-height:14.2px;color:var(--text);width:280px}
.client-name{font-size:12px;color:var(--orange-deep)}
.quote-mark{font-family:Georgia,serif;font-size:44px;font-weight:700;color:#b5b5b5;line-height:1}

/* footer */
.site-footer{left:0;top:979px;width:960px;height:221px;background:var(--footer)}
.footer-title{font-family:"Oswald",Arial,sans-serif;font-size:16px;color:var(--orange)}
.footer-nav a{display:block;font-family:"Oswald",Arial,sans-serif;font-size:16px;color:var(--white);text-decoration:none;height:25px;line-height:25px}
.footer-nav a.current{color:var(--orange)}
.blog-item{display:flex;gap:6px;height:45px}
.blog-thumb{width:50px;height:37px;background:linear-gradient(180deg,#e8e8e8,#c9c9c9)}
.blog-text{font-size:10.8px;color:var(--white);line-height:13.5px}
.blog-text .by{color:var(--orange)}
.contact-lines{font-size:11.5px;line-height:21.7px;color:var(--white)}
.social{width:37px;height:37px;border-radius:50%;border:2px solid var(--orange)}
.footer-bar{left:0;top:1161px;width:960px;height:39px;background:var(--footer);border-top:1px solid var(--footer-line);text-align:center;line-height:38px;font-size:9.5px;color:var(--white)}
.footer-bar b{color:var(--orange)}
</style>
</head>
<body>

<header class="abs site-header">
  <div class="abs brand"><span class="brand-dot"></span><span class="brand-name">vextra</span></div>
  <nav class="abs main-nav">
    <a class="active" href="#">Home</a><a href="#">Features</a><a href="#">Work</a><a href="#">Pricing</a><a href="#">Shop</a><a href="#">Contact</a>
  </nav>
</header>

<section class="abs hero" role="img" aria-label="Blurred warm-toned photo of a desk with a keyboard"></section>
<h1 class="abs hero-title">Unique experiences for<br>web &amp; mobile</h1>
<div class="abs hero-devices" role="img" aria-label="Laptop and desktop monitor showing the app's multimedia keys and client devices layout screens"></div>

<!-- features -->
<div class="abs feature-icon" style="left:71px;top:347px">
  <svg width="30" height="30" viewBox="0 0 30 30"><path d="M5 24 C8 10 16 5 26 5 C26 16 20 24 8 23 Z" fill="none" stroke="#fff" stroke-width="2.4"/><path d="M5 25 L17 14" stroke="#fff" stroke-width="2.4"/></svg>
</div>
<div class="abs feature" style="left:141px;top:344px">
  <h2 class="feature-title">Expressive Design</h2>
  <p class="feature-text">Lorem Ipsum is simply dummy text of the printing and typesetting industry. Lorem Ipsum has been the industry's standard dummy text ever.Lorem Ipsum is simply dummy text</p>
</div>

<div class="abs feature-icon" style="left:479px;top:347px">
  <svg width="32" height="28" viewBox="0 0 32 28"><path d="M2 10 A20 20 0 0 1 30 10" fill="none" stroke="#fff" stroke-width="3"/><path d="M7 15 A13 13 0 0 1 25 15" fill="none" stroke="#fff" stroke-width="3"/><path d="M11.5 20 A7 7 0 0 1 20.5 20" fill="none" stroke="#fff" stroke-width="3"/><circle cx="16" cy="24.5" r="2.3" fill="#fff"/></svg>
</div>
<div class="abs feature" style="left:547px;top:344px">
  <h2 class="feature-title">Huge Analytics</h2>
  <p class="feature-text" style="width:335px;margin-top:2px">Lorem Ipsum is simply dummy text of the printing and typesetting industry. Lorem Ipsum has been the industry's standard dummy text ever.Lorem Ipsum is simply dummy text.</p>
</div>

<div class="abs feature-icon" style="left:71px;top:460px">
  <svg width="32" height="22" viewBox="0 0 32 22"><path d="M8 21 H25 A6 6 0 0 0 25 9 A8 8 0 0 0 10 7 A7 7 0 0 0 8 21 Z" fill="#fff"/></svg>
</div>
<div class="abs feature" style="left:141px;top:457px">
  <h2 class="feature-title">Easy Configuration</h2>
  <p class="feature-text">Lorem Ipsum is simply dummy text of the printing and typesetting industry. Lorem Ipsum has been the industry's standard dummy text ever.Lorem Ipsum is simply dummy text</p>
</div>

<div class="abs feature-icon" style="left:479px;top:460px">
  <svg width="30" height="24" viewBox="0 0 30 24"><rect x="1" y="19" width="4" height="4" fill="#fff"/><rect x="7" y="16" width="4" height="7" fill="#fff"/><rect x="13" y="12" width="4" height="11" fill="#fff"/><rect x="19" y="7" width="4" height="16" fill="#fff"/><rect x="25" y="1" width="4" height="22" fill="#fff"/></svg>
</div>
<div class="abs feature" style="left:547px;top:462px">
  <h2 class="feature-title">Tuned to Perfection</h2>
  <p class="feature-text" style="width:335px;margin-top:2px">Lorem Ipsum is simply dummy text of the printing and typesetting industry. Lorem Ipsum has been the industry's standard dummy text ever.Lorem Ipsum is simply dummy text.</p>
</div>

<!-- options -->
<section class="abs options"></section>
<div class="abs options-shot" role="img" aria-label="Screenshot of the app's device pairing and client devices layout window"></div>
<div class="abs circle-icon" style="left:487px;top:581px">
  <svg width="24" height="22" viewBox="0 0 24 22"><path d="M2 11 L12 2 L22 11" fill="none" stroke="#fff" stroke-width="2.6"/><path d="M5 10 V20 H10 V14 H14 V20 H19 V10" fill="#fff"/></svg>
</div>
<h2 class="abs section-title" style="left:533px;top:588px"><span class="hl">VEXTRA</span> Very powerful options built right in</h2>
<p class="abs options-text" style="left:490px;top:624px">Lorem Ipsum is simply dummy text of the printing and typesetting industry. Lorem Ipsum has been the industry's standard dummy text ever since the 1500s, when an unknown printer took a galley of type and scrambled it to make a type.</p>
<ul class="abs check-list" style="left:488px;top:683px">
  <li><svg width="13" height="10" viewBox="0 0 13 10"><path d="M1 5 L5 9 L12 1" fill="none" stroke="#999" stroke-width="2"/></svg>Lorem Ipsum is simply dummy text</li>
  <li><svg width="13" height="10" viewBox="0 0 13 10"><path d="M1 5 L5 9 L12 1" fill="none" stroke="#999" stroke-width="2"/></svg>Lorem Ipsum is simply dummy text</li>
  <li><svg width="13" height="10" viewBox="0 0 13 10"><path d="M1 5 L5 9 L12 1" fill="none" stroke="#999" stroke-width="2"/></svg>Lorem Ipsum is simply dummy text</li>
</ul>
<ul class="abs check-list" style="left:697px;top:683px">
  <li><svg width="13" height="10" viewBox="0 0 13 10"><path d="M1 5 L5 9 L12 1" fill="none" stroke="#999" stroke-width="2"/></svg>Lorem Ipsum is simply dummy text</li>
  <li><svg width="13" height="10" viewBox="0 0 13 10"><path d="M1 5 L5 9 L12 1" fill="none" stroke="#999" stroke-width="2"/></svg>Lorem Ipsum is simply dummy text</li>
  <li><svg width="13" height="10" viewBox="0 0 13 10"><path d="M1 5 L5 9 L12 1" fill="none" stroke="#999" stroke-width="2"/></svg>Lorem Ipsum is simply dummy text</li>
</ul>
<p class="abs options-text" style="left:490px;top:749px">Lorem Ipsum is simply dummy text of the printing and typesetting industry. Lorem Ipsum has been the industry's standard dummy text ever since the 1500s.</p>
<a class="abs learn-more" style="left:819px;top:787px" href="#">Learn More</a>

<!-- testimonials -->
<div class="abs circle-icon" style="left:371px;top:842px">
  <svg width="22" height="22" viewBox="0 0 22 22"><rect x="1" y="9" width="5" height="12" fill="#fff"/><path d="M8 9 L12 1 C14 1 15 3 14 6 L13 8 H20 C21 8 22 9 21.5 10.5 L19 19.5 C18.7 20.5 18 21 17 21 H8 Z" fill="#fff"/></svg>
</div>
<h2 class="abs section-title" style="left:421px;top:846px"><span class="hl">Client</span> Testimonial</h2>

<div class="abs testimonial-photo" style="left:84px;top:892px" role="img" aria-label="Portrait photo of a smiling client"></div>
<span class="abs quote-mark" style="left:156px;top:890px">&#8220;</span>
<p class="abs quote-text" style="left:182px;top:893px">Lorem Ipsum is simply dummy text of the printing and typesetting industry. Lorem Ipsum has been the industry's standard dummy text ever since the 1500s, when an unknown printer took.</p>
<span class="abs client-name" style="left:365px;top:939px">- Client Name</span>
<span class="abs quote-mark" style="left:444px;top:935px">&#8221;</span>

<div class="abs testimonial-photo" style="left:495px;top:892px" role="img" aria-label="Portrait photo of a smiling client"></div>
<span class="abs quote-mark" style="left:567px;top:890px">&#8220;</span>
<p class="abs quote-text" style="left:593px;top:893px">Lorem Ipsum is simply dummy text of the printing and typesetting industry. Lorem Ipsum has been the industry's standard dummy text ever since the 1500s, when an unknown printer took.</p>
<span class="abs client-name" style="left:776px;top:939px">- Client Name</span>
<span class="abs quote-mark" style="left:855px;top:935px">&#8221;</span>

<!-- footer -->
<footer class="abs site-footer"></footer>
<nav class="abs footer-nav" style="left:80px;top:986px">
  <a class="current" href="#">Home</a><a href="#">Features</a><a href="#">Work</a><a href="#">Pricing</a><a href="#">Shop</a><a href="#">Contact</a>
</nav>

<h3 class="abs footer-title" style="left:276px;top:988px">From the Blog</h3>
<div class="abs" style="left:274px;top:1017px">
  <div class="blog-item"><div class="blog-thumb" role="img" aria-label="Blog post thumbnail"></div><p class="blog-text">Lorem Ipsum is simply dummy<br>19 Oct 2012 | <span class="by">By Admin</span></p></div>
  <div class="blog-item"><div class="blog-thumb" role="img" aria-label="Blog post thumbnail"></div><p class="blog-text">Lorem Ipsum is simply dummy<br>19 Oct 2012 | <span class="by">By Admin</span></p></div>
  <div class="blog-item"><div class="blog-thumb" role="img" aria-label="Blog post thumbnail"></div><p class="blog-text">Lorem Ipsum is simply dummy<br>19 Oct 2012 | <span class="by">By Admin</span></p></div>
</div>

<h3 class="abs footer-title" style="left:494px;top:988px">Get In Touch</h3>
<p class="abs contact-lines" style="left:491px;top:1012px">Office No., Building name,<br>Area name,<br>City, State, Country<br>Call : +44 100 200 3000<br>Fax : +44 100 200 3000<br>Email : info@vextra-mail.com</p>

<h3 class="abs footer-title" style="left:710px;top:988px">Get In Touch</h3>
<span class="abs social" style="left:715px;top:1020px"></span>
<span class="abs social" style="left:771px;top:1020px"></span>
<span class="abs social" style="left:827px;top:1020px"></span>
<span class="abs social" style="left:715px;top:1076px"></span>
<span class="abs social" style="left:771px;top:1076px"></span>
<span class="abs social" style="left:827px;top:1076px"></span>

<div class="abs footer-bar">© <b>VEXTRA</b> - 2014. All Rights Reserved.</div>

</body>
</html>
```